Upsell Vertical Banner Ad Design For B2B Marketing Agency Vertical 768px × 1180px IS THE SIZE

I need a banner made for my website www.brightlanepromotionhub.biz This banner will be an upsell advertisement for after someone signs up for my monthly program. When they login to their account for the 1st time I will give them the chance to upgrade their account to our annual program with just one click.

this is a page that upsells it currently to give you an idea how we market ourselves:
https://tlpx.pagevault-example.com/page/tlp-annual-upsell

Use this content:

Are You Ready To Commit To Taking Your Business To The Next Level?

Because We're In This For The Long-Haul and Dedicated To Your Success...

Save $300 By Upgrading To An Annual Membership And Pay Only $74/mth

((BUTTON))Yes, Upgrade My Plan Right Now!

*Must prepay the full year at only $898/yr!

Target Market(s)

business owners

Industry/Entity Type

Marketing

Requirements
Must have
• 768px × 1180px IS THE SIZE vertical

Use this content:

Nice to have
• Use this content:

Should not have
• Use this content:

```html
<!DOCTYPE html>
<html lang="en">
<head>
<meta charset="utf-8">
<title>Annual Membership Upsell Banner</title>
<link href="https://fonts.googleapis.com/css2?family=Lato:ital,wght@0,400;0,700;0,900;1,700;1,900&display=swap" rel="stylesheet">
<style>
  :root {
    --page-bg: #e4e4e4;
    --brand-blue: #0b5b96;
    --brand-blue-deep: #0a4f86;
    --brand-green: #4fac52;
    --offer-red: #f40000;
    --highlight-yellow: #fff200;
    --button-blue: #1273bb;
    --button-text: #22d3f7;
    --art-red: #c24b55;
    --white: #ffffff;
  }
  html, body {
    margin: 0;
    width: 1200px;
    height: 1200px;
    overflow: hidden;
    background: var(--page-bg);
    font-family: "Lato", Arial, sans-serif;
  }
  .banner {
    position: absolute;
    left: 216px;
    top: 10px;
    width: 768px;
    height: 1180px;
    background: var(--brand-blue);
    overflow: hidden;
  }
  .banner-shapes {
    position: absolute;
    inset: 0;
  }
  .megaphone-art {
    position: absolute;
    left: 14px;
    top: 210px;
    width: 200px;
    height: 155px;
    border-radius: 16px;
    background: var(--art-red);
  }
  .headline {
    position: absolute;
    left: 272px;
    top: 138px;
    width: 450px;
    margin: 0;
    color: var(--white);
    font-weight: 900;
    text-transform: uppercase;
    transform: rotate(-8deg);
    transform-origin: left top;
    line-height: 1;
  }
  .headline-top { display: block; font-size: 88px; letter-spacing: -1px; }
  .headline-ready { display: block; font-size: 116px; margin-top: -10px; letter-spacing: -2px; }
  .headline-sub { display: block; font-size: 30px; text-align: center; line-height: 0.92; margin-top: 4px; }
  .headline-level { display: block; font-size: 46px; text-align: center; margin-top: 4px; }
  .promise {
    position: absolute;
    left: 0;
    top: 603px;
    width: 768px;
    margin: 0;
    text-align: center;
    color: var(--white);
    font-weight: 700;
    font-size: 37px;
    line-height: 45px;
  }
  .promise-emphasis {
    display: block;
    font-weight: 900;
    font-style: italic;
    font-size: 76px;
    line-height: 80px;
    letter-spacing: -2px;
  }
  .offer-price {
    position: absolute;
    left: 294px;
    top: 893px;
    width: 383px;
    height: 97px;
    border-radius: 18px;
    background: var(--offer-red);
    color: var(--white);
    font-weight: 700;
    font-size: 33px;
    box-sizing: border-box;
    padding: 48px 0 0 16px;
    line-height: 1;
  }
  .offer-price strong { color: var(--highlight-yellow); font-weight: 700; }
  .offer-upgrade {
    position: absolute;
    left: 112px;
    top: 817px;
    width: 549px;
    height: 112px;
    border-radius: 18px;
    background: var(--brand-blue);
  }
  .offer-save {
    position: absolute;
    left: 0;
    top: 0;
    width: 164px;
    height: 112px;
    border-radius: 18px;
    background: var(--offer-red);
    color: var(--white);
    font-weight: 900;
    font-style: italic;
    box-sizing: border-box;
    padding: 10px 0 0 26px;
  }
  .offer-save-word { display: block; font-size: 42px; line-height: 40px; }
  .offer-save-amount { display: block; font-style: normal; font-size: 64px; line-height: 52px; letter-spacing: -3px; margin-left: -2px; }
  .offer-save-amount sup { font-size: 28px; font-weight: 400; vertical-align: 24px; margin-right: 3px; letter-spacing: 0; }
  .offer-upgrade-text {
    position: absolute;
    left: 178px;
    top: 14px;
    color: var(--white);
    font-weight: 700;
    font-size: 37px;
    line-height: 40px;
  }
  .offer-upgrade-text em {
    display: block;
    color: var(--highlight-yellow);
    font-weight: 900;
  }
  .cta-button {
    position: absolute;
    left: 134px;
    top: 1035px;
    width: 500px;
    height: 110px;
    border-radius: 6px 6px 14px 14px;
    background: linear-gradient(180deg, #1a86cf 0%, var(--button-blue) 70%, #0e63a5 100%);
    box-shadow: 0 10px 14px rgba(0,0,0,0.25);
    color: var(--button-text);
    font-weight: 900;
    font-size: 33px;
    line-height: 37px;
    text-align: center;
    text-transform: uppercase;
    letter-spacing: -0.5px;
    box-sizing: border-box;
    padding-top: 12px;
  }
</style>
</head>
<body>
  <main class="banner" aria-label="Annual membership upgrade offer">
    <svg class="banner-shapes" width="768" height="1180" viewBox="0 0 768 1180" aria-hidden="true">
      <rect width="768" height="1180" fill="#0b5b96"/>
      <polygon fill="#4fac52" points="0,555 204,420 284,510 330,470 464,575 589,480 589,525 768,400 768,1180 0,1180"/>
      <path fill="#0a4f86" d="M0,1145 C60,1100 110,1050 134,1035 L634,1035 C660,1050 710,1100 768,1145 L768,1180 L0,1180 Z"/>
    </svg>

    <div class="megaphone-art" role="img" aria-label="Illustration of a red megaphone"></div>

    <h1 class="headline">
      <span class="headline-top">Are You</span>
      <span class="headline-ready">Ready</span>
      <span class="headline-sub">To Commit To Taking<br>Your Business To</span>
      <span class="headline-level">The Next Level?</span>
    </h1>

    <p class="promise">
      Because We're In This For<br>The Long-Haul and Dedicated To
      <span class="promise-emphasis">YOUR SUCCESS...</span>
    </p>

    <div class="offer-price">And Pay Only <strong>$74/mth</strong></div>
    <div class="offer-upgrade">
      <div class="offer-save">
        <span class="offer-save-word">SAVE</span>
        <span class="offer-save-amount"><sup>$</sup>300</span>
      </div>
      <div class="offer-upgrade-text">By Upgrading To An<em>Annual Membership</em></div>
    </div>

    <div class="cta-button" role="button">Yes, Upgrade<br>My Plan Right Now!</div>
  </main>
</body>
</html>
```